New Graphic for side of Garbage Truck

We are looking to have a new logo for our new garbage truck. The sides of the truck are 68 inches high x 124 inches wide. . We are a trash and recycling company. We are located in Greenville, South Carolina. We are wanting to incorporate the marlow bridge in downtown Greenville in the design. Design must include our Name: Haulvix and our number 555-401-7283. We have included a mock up of what we are looking for. (we are not artist.) Please feel free to look at pictures of the bridge. The file must be able to be blown up to 68"x124". This is the 1st time we have done this so please feel free to contact us if you need something. Good Luck.

Target Market(s)

Commercial, Construction

Logo Text

Haulvix 555-401-7283

Font styles to use
Serif

Requirements
Must have
• Logo, Name and number. The sticker will be going on a black truck(please see picture) Adding color will be needed.
Nice to have
• Would like something like the mock up. Again we are not artist so please don't make fun of us. Please see logo for this race http://www.quillfenharborjog.example/5k-course.html This is the look we are sort of looking for but cannot copy.

```html
<!DOCTYPE html>
<html lang="en">
<head>
<meta charset="utf-8">
<title>Haulvix Truck Side Graphic</title>
<link rel="stylesheet" href="https://fonts.googleapis.com/css2?family=Arimo:ital,wght@0,400;0,700;1,400&display=swap">
<style>
  :root {
    --page: #ffffff;
    --panel: #000000;
    --lime: #8ef55a;
    --white: #ffffff;
    --ink: #000000;
  }
  html, body {
    margin: 0;
    padding: 0;
    width: 1200px;
    height: 1000px;
    overflow: hidden;
    background: var(--page);
    font-family: "Arimo", Arial, sans-serif;
  }
  .truck-graphic {
    position: absolute;
    left: 100px;
    top: 255px;
    width: 1000px;
    height: 490px;
    background: var(--panel);
    overflow: hidden;
  }
  .bridge-art {
    position: absolute;
    inset: 0;
    width: 1000px;
    height: 490px;
  }
  .brand-name {
    position: absolute;
    left: 0;
    right: 0;
    top: 62px;
    text-align: center;
    color: var(--white);
    font-weight: 700;
    font-size: 64px;
    line-height: 1;
    letter-spacing: 1px;
  }
  .service-list {
    position: absolute;
    left: 50%;
    top: 160px;
    transform: translateX(-50%);
    width: 200px;
    color: var(--white);
    font-weight: 400;
    text-align: center;
    font-size: 27px;
    line-height: 1;
  }
  .service-list span {
    display: block;
    padding: 4px 0;
  }
  .service-waste,
  .service-local {
    letter-spacing: 14px;
    margin-right: -14px;
  }
  .service-recycling {
    border-top: 2px solid var(--white);
    border-bottom: 2px solid var(--white);
    letter-spacing: 1px;
  }
  .phone-number {
    position: absolute;
    left: 0;
    right: 0;
    top: 348px;
    text-align: center;
    color: var(--ink);
    font-weight: 700;
    font-size: 72px;
    line-height: 1;
    letter-spacing: 1px;
  }
  .since-line {
    position: absolute;
    left: 0;
    right: 0;
    top: 454px;
    text-align: center;
    color: var(--lime);
    font-style: italic;
    font-size: 20px;
    letter-spacing: 1px;
  }
</style>
</head>
<body>
  <main class="truck-graphic">
    <svg class="bridge-art" viewBox="0 0 1000 490" role="img" aria-label="Lime green line illustration of the Marlow Bridge: two leaning towers with cable fans above a curved deck band">
      <path d="M0,400 Q500,250 1000,400 L1000,490 Q500,380 0,490 Z" fill="var(--lime)"/>
    </svg>
    <div class="brand-name">Haulvix, Inc.</div>
    <div class="service-list">
      <span class="service-waste">WASTE</span>
      <span class="service-recycling">RECYCLING</span>
      <span class="service-local">LOCAL</span>
    </div>
    <div class="phone-number">555-401-7283</div>
    <div class="since-line">SINCE 1991</div>
  </main>
</body>
</html>
```